Business Card Design Project

I help solve problems that people have with real estate, so I buy homes for cash that they no longer want, can't afford, inherited, etc. and fix and sell them or rent them or take over mortgage payments. See website: www.quickhomepurchase-example.com

Industry/Entity Type

Real Estate

Contact Information for Business Card

Not exactly sure. Looking for a design that either is similar to the website www.quickhomepurchase-example.com or that reflects what I do as described below. If it can look a little luxurious to show I can buy the houses for cash and I fix them and sell them, it's a bonus. I seem to like some of the higher end things like foil or black or something that makes it stand out.

Font styles to use
Serif

Requirements
Nice to have
• I seem to like black or clear. I like things to stand out and be different.

```html
<!DOCTYPE html>
<html lang="en">
<head>
<meta charset="utf-8">
<title>Renewed Homes – Business Card</title>
<link rel="stylesheet" href="https://fonts.googleapis.com/css2?family=Arimo:wght@400;700&display=swap">
<style>
  :root {
    --stage: #1e1e1e;
    --card-white: #ffffff;
    --green: #4f9a32;
    --green-top: #55903c;
    --green-bottom: #7bb943;
    --ink: #222222;
    --rule: #9a9a9a;
    --on-green: #ffffff;
  }
  * { margin: 0; padding: 0; box-sizing: border-box; }
  html, body { width: 1200px; height: 900px; overflow: hidden; }
  body {
    background: var(--stage);
    font-family: "Arimo", Arial, sans-serif;
    position: relative;
  }
  .card {
    position: absolute;
    top: 170px;
    width: 347px;
    height: 561px;
    box-shadow: 3px 4px 8px rgba(0,0,0,0.55);
    text-align: center;
  }
  .card--front { left: 259px; background: var(--card-white); }
  .card--back {
    left: 631px;
    background: linear-gradient(180deg, var(--green-top) 0%, var(--green-bottom) 100%);
    color: var(--on-green);
  }
  .brand-name {
    position: absolute;
    left: 0; right: 0;
    font-weight: 700;
    text-transform: uppercase;
    line-height: 0.95;
    letter-spacing: 0.5px;
  }
  .card--front .brand-name { top: 146px; font-size: 46px; color: var(--green); }
  .card--back .brand-name { top: 128px; font-size: 46px; color: var(--on-green); }

  .person { position: absolute; left: 0; right: 0; top: 380px; }
  .person__name { font-size: 20px; font-weight: 700; color: var(--green); letter-spacing: 0.3px; }
  .person__role { font-size: 15px; color: var(--ink); margin-top: 2px; }

  .contact-divider {
    position: absolute; top: 439px; left: 92px; width: 164px; height: 14px;
    display: flex; align-items: center; gap: 5px;
  }
  .contact-divider .rule { flex: 1; height: 1px; background: var(--rule); }
  .contact-divider svg { width: 12px; height: 12px; fill: var(--green); }

  .contact-list {
    position: absolute; left: 0; right: 0; top: 459px;
    list-style: none; font-size: 16px; color: var(--ink); line-height: 20.5px;
  }

  .services {
    position: absolute; left: 0; right: 0; top: 284px;
    list-style: none; font-size: 21px; font-weight: 700; line-height: 37px;
  }
  .back-rule {
    position: absolute; top: 396px; left: 24px; right: 28px; height: 1px;
    background: rgba(255,255,255,0.8);
  }
  .about {
    position: absolute; left: 0; right: 0; top: 408px;
    font-size: 16px; line-height: 20.3px;
  }
</style>
</head>
<body>
  <section class="card card--front">
    <div class="brand-name">Renewed<br>Homes</div>
    <div class="person">
      <div class="person__name">DANIEL CARTER</div>
      <div class="person__role">Managing Director</div>
    </div>
    <div class="contact-divider">
      <span class="rule"></span>
      <svg viewBox="0 0 24 24" aria-label="phone"><path d="M6.6 10.8a15 15 0 0 0 6.6 6.6l2.2-2.2c.3-.3.7-.4 1-.2 1.1.4 2.3.6 3.6.6.6 0 1 .4 1 1V20c0 .6-.4 1-1 1A17 17 0 0 1 3 4c0-.6.4-1 1-1h3.5c.6 0 1 .4 1 1 0 1.3.2 2.5.6 3.6.1.3 0 .7-.2 1z"/></svg>
      <svg viewBox="0 0 24 24" aria-label="email"><path d="M2 5h20v14H2z M3 6l9 7 9-7" fill="var(--green)"/><path d="M3 6.5l9 7 9-7" fill="none" stroke="#fff" stroke-width="1.6"/></svg>
      <svg viewBox="0 0 24 24" aria-label="website"><circle cx="12" cy="12" r="10"/><path d="M2 12h20M12 2c3 3 3 17 0 20M12 2c-3 3-3 17 0 20" fill="none" stroke="#fff" stroke-width="1.4"/></svg>
      <span class="rule"></span>
    </div>
    <ul class="contact-list">
      <li>555-010-SOLD</li>
      <li>info@renewedhomes-example.com</li>
      <li>www.quickhomepurchase-example.com</li>
    </ul>
  </section>

  <section class="card card--back">
    <div class="brand-name">Renewed<br>Homes</div>
    <ul class="services">
      <li>BUY A HOME</li>
      <li>FACING FORECLOSURE</li>
      <li>SELL A HOME</li>
    </ul>
    <div class="back-rule"></div>
    <p class="about">
      We are a group of Real Estate Investors<br>
      that are looking to<br>
      buy and sell homes in your area.<br>
      If you are buying or selling a home<br>
      in Illinois we want to talk to you.<br>
      Call Us Now 555-010-SOLD
    </p>
  </section>
</body>
</html>
```